Shoes, Handbags and Accessories

The main business of the company are shoes and then handbags, jewellery and scarves to accessorize.

The design I am looking for is a "shabby chic" design, cursive font, perhaps with a vintage country feel to it.

Target Market(s)

Age group are more for the 25+, but more so 35+ ladies.

Industry/Entity Type

Business

Contact Information for Business Card

Lace Lane Boutique & Accessories
Marlene Toohey - P.O. Box 482, Kulbari W.A. 6281
Ph: (08) 97314426 fax: (08) 97314427 Mobile: 0419273561
Email:lacelane@brindanet.com.au
Web: www.lacelaneboutique.com.au
Like us on Chatterbook (Chatterbook logo)

Requirements
Must have
• As already described. A "faded" picture background is also another feature I like, but I don't want to create a cluttered look about the business card.
Nice to have
• Classy, stylish and comfortable shoes.

```html
<!DOCTYPE html>
<html lang="en">
<head>
<meta charset="utf-8">
<title>Lace Lane Boutique &amp; Accessories – Business Card</title>
<link rel="stylesheet" href="https://fonts.googleapis.com/css2?family=Pinyon+Script&family=Noto+Serif:wght@700&family=Open+Sans:wght@400;600&display=swap">
<style>
  :root {
    --page-bg: #e9e6e1;
    --card-top: #d8b887;
    --card-mid: #eadbc3;
    --card-bottom: #f3f0ea;
    --brand-brown: #6b4a26;
    --name-brown: #5b3a1c;
    --text-dark: #3b3631;
    --social-square: #7a5a2c;
    --shoe-beige: #c9b48f;
    --shoe-burgundy: #5e2a2a;
    --shoe-grey: #5d5d5d;
  }
  * { box-sizing: border-box; margin: 0; padding: 0; }
  html, body {
    width: 1200px; height: 918px; overflow: hidden;
    background: var(--page-bg);
  }
  .card {
    position: absolute; left: 350px; top: 50px;
    width: 500px; height: 818px;
    background: linear-gradient(180deg, var(--card-top) 0%, var(--card-mid) 32%, var(--card-bottom) 55%, var(--card-bottom) 100%);
    box-shadow: 0 6px 24px rgba(0,0,0,0.18);
    border-radius: 4px;
    overflow: hidden;
  }
  .brand {
    position: absolute; left: 48px; top: 70px;
    font-family: "Pinyon Script", cursive;
    font-weight: 400;
    color: var(--brand-brown);
    line-height: 1.05;
  }
  .brand-line { display: block; font-size: 62px; }
  .brand-line--second { padding-left: 60px; font-size: 56px; }
  .social {
    position: absolute; right: 44px; top: 380px;
    text-align: right;
    font-family: "Open Sans", sans-serif;
    font-size: 14px; line-height: 1.25;
    color: var(--text-dark);
  }
  .social-square {
    display: block; margin: 8px 0 0 auto;
    width: 44px; height: 44px;
    background: var(--social-square);
    border-radius: 4px;
  }
  .contact {
    position: absolute; left: 48px; top: 400px;
    font-family: "Open Sans", sans-serif;
    color: var(--text-dark);
  }
  .contact-name {
    font-family: "Noto Serif", serif;
    font-weight: 700;
    font-size: 28px;
    color: var(--name-brown);
    margin-bottom: 8px;
  }
  .contact-line { font-size: 15px; line-height: 1.45; }
  .shoe-row {
    position: absolute; left: 40px; right: 40px; bottom: 50px;
    display: flex; justify-content: space-between; align-items: flex-end;
  }
  .shoe { display: block; width: 120px; height: 110px; }
</style>
</head>
<body>
  <main class="card">
    <h1 class="brand">
      <span class="brand-line">Lace Lane Boutique</span>
      <span class="brand-line brand-line--second">&amp; Accessories</span>
    </h1>

    <aside class="social">
      <p>Like us on</p>
      <p>Chatterbook</p>
      <span class="social-square"></span>
    </aside>

    <section class="contact">
      <h2 class="contact-name">Marlene Toohey</h2>
      <p class="contact-line">P.O. Box 482, Kulbari W.A. 6281</p>
      <p class="contact-line">Ph: (08) 97314426 fax: (08) 97314427</p>
      <p class="contact-line">Mobile: 0419273561</p>
      <p class="contact-line">Email: lacelane@brindanet.com.au</p>
      <p class="contact-line">Web: www.lacelaneboutique.com.au</p>
    </section>

    <div class="shoe-row">
      <svg class="shoe" role="img" aria-label="Photo of a beige court shoe" viewBox="0 0 120 110">
        <defs><radialGradient id="shoe-beige-fill"><stop offset="0" stop-color="#d9c7a4"/><stop offset="1" stop-color="#a88f66"/></radialGradient></defs>
        <rect x="4" y="20" width="112" height="86" rx="18" fill="url(#shoe-beige-fill)"/>
      </svg>
      <svg class="shoe" role="img" aria-label="Photo of a burgundy strap shoe" viewBox="0 0 120 110">
        <defs><radialGradient id="shoe-burgundy-fill"><stop offset="0" stop-color="#7a3a38"/><stop offset="1" stop-color="#3e1a1a"/></radialGradient></defs>
        <rect x="4" y="20" width="112" height="86" rx="18" fill="url(#shoe-burgundy-fill)"/>
      </svg>
      <svg class="shoe" role="img" aria-label="Photo of a grey ankle boot" viewBox="0 0 120 110">
        <defs><radialGradient id="shoe-grey-fill"><stop offset="0" stop-color="#7d7d7d"/><stop offset="1" stop-color="#3f3f3f"/></radialGradient></defs>
        <rect x="4" y="20" width="112" height="86" rx="18" fill="url(#shoe-grey-fill)"/>
      </svg>
    </div>
  </main>
</body>
</html>
```